Commercial Real Estate

We need a business card design for a new commercial real estate business that specializes in apartment building brokerage. Not individual units but the entire complex. We find and represent the owners existing buildings and well as new buyers for those buildings. The design should convey trust, integrity, knowledge and growth. It should be easily read.

Target Market(s)

40 to 65 years old

Industry/Entity Type

Real Estate

```html
<!DOCTYPE html>
<html lang="en">
<head>
<meta charset="utf-8">
<title>Harborline Property Investments – Business Card</title>
<link rel="stylesheet" href="https://fonts.googleapis.com/css2?family=Open+Sans:wght@400;600;700&display=swap">
<style>
  :root {
    --backdrop: #d6d7d9;
    --card: #ffffff;
    --band: #ecebe6;
    --teal: #6ec9cb;
    --slate: #4f5d5d;
    --slate-soft: #5d6767;
    --ink: #111111;
    --icon-bg: #e3f3f3;
  }
  * { box-sizing: border-box; margin: 0; padding: 0; }
  html, body {
    width: 1200px;
    height: 1200px;
    overflow: hidden;
    background: var(--backdrop);
    font-family: "Open Sans", Arial, sans-serif;
  }
  .card {
    position: absolute;
    left: 150px;
    top: 342px;
    width: 901px;
    height: 514px;
    background: var(--card);
    overflow: hidden;
  }
  .card-bands { position: absolute; inset: 0; }
  .building-art {
    position: absolute;
    left: 96px;
    top: 32px;
    width: 222px;
    height: 406px;
    border-radius: 6px;
    background: linear-gradient(180deg, var(--teal) 0%, #5fb3b5 70%, var(--slate) 100%);
  }
  .brand {
    position: absolute;
    left: 518px;
    top: 26px;
    width: 346px;
    text-align: right;
    color: var(--slate);
  }
  .brand-name {
    font-size: 50px;
    font-weight: 700;
    line-height: 1.1;
    letter-spacing: 0.5px;
  }
  .brand-tagline {
    margin-top: 8px;
    font-size: 18px;
    font-weight: 700;
    letter-spacing: 3.2px;
  }
  .person {
    position: absolute;
    left: 518px;
    top: 222px;
  }
  .person-name {
    font-size: 35px;
    font-weight: 700;
    color: var(--ink);
    line-height: 1.2;
  }
  .person-title {
    font-size: 24px;
    color: var(--slate-soft);
    line-height: 1.3;
  }
  .contact-list {
    position: absolute;
    right: 36px;
    top: 338px;
    list-style: none;
    text-align: right;
    font-size: 22px;
    color: var(--ink);
    line-height: 32px;
  }
  .contact-item {
    display: flex;
    justify-content: flex-end;
    align-items: flex-start;
    gap: 12px;
  }
  .contact-item .icon {
    width: 24px;
    height: 24px;
    margin-top: 4px;
    flex: none;
  }
  .contact-item .spacer { width: 24px; flex: none; }
  .website {
    position: absolute;
    left: 44px;
    top: 464px;
    display: flex;
    align-items: center;
    gap: 12px;
    font-size: 23px;
    color: var(--ink);
  }
  .website .icon { width: 22px; height: 22px; }
</style>
</head>
<body>
  <main class="card">
    <svg class="card-bands" viewBox="0 0 901 514" aria-hidden="true">
      <polygon points="0,0 468,0 0,276" fill="var(--band)"/>
      <polygon points="901,144 901,514 246,514" fill="var(--band)"/>
    </svg>

    <div class="building-art" role="img" aria-label="Illustration of a tall teal apartment tower with dark windows, flaring outward at the top"></div>

    <header class="brand">
      <div class="brand-name">Harborline</div>
      <div class="brand-tagline">Property Investments</div>
    </header>

    <section class="person">
      <div class="person-name">Your Name</div>
      <div class="person-title">Your title</div>
    </section>

    <ul class="contact-list">
      <li class="contact-item">
        <span>555 555 5555</span>
        <svg class="icon" viewBox="0 0 24 24" aria-hidden="true">
          <circle cx="12" cy="12" r="12" fill="var(--icon-bg)"/>
          <path d="M7 8c1-2 3-2 3-1l1 2-1 1c1 2 2 3 4 4l1-1 2 1c1 0 1 2-1 3-4 0-9-5-9-9z" fill="var(--teal)"/>
        </svg>
      </li>
      <li class="contact-item">
        <span>555 555 5555</span>
        <svg class="icon" viewBox="0 0 24 24" aria-hidden="true">
          <circle cx="12" cy="12" r="12" fill="var(--icon-bg)"/>
          <rect x="8" y="5" width="8" height="5" fill="var(--teal)"/>
          <rect x="6" y="10" width="12" height="6" rx="1" fill="var(--teal)"/>
          <rect x="8" y="14" width="8" height="5" fill="#ffffff" stroke="var(--teal)" stroke-width="1"/>
        </svg>
      </li>
      <li class="contact-item">
        <span>Your company address</span>
        <svg class="icon" viewBox="0 0 24 24" aria-hidden="true">
          <circle cx="12" cy="12" r="12" fill="var(--icon-bg)"/>
          <path d="M5 12l7-6 7 6h-2v6h-4v-4h-2v4H7v-6z" fill="var(--teal)"/>
        </svg>
      </li>
      <li class="contact-item">
        <span>City zipcode</span>
        <span class="spacer"></span>
      </li>
      <li class="contact-item">
        <span>your email address</span>
        <svg class="icon" viewBox="0 0 24 24" aria-hidden="true">
          <circle cx="12" cy="12" r="12" fill="var(--icon-bg)"/>
          <rect x="6" y="8" width="12" height="9" fill="var(--teal)"/>
          <path d="M6 8l6 5 6-5" fill="none" stroke="#ffffff" stroke-width="1.2"/>
        </svg>
      </li>
    </ul>

    <div class="website">
      <svg class="icon" viewBox="0 0 24 24" aria-hidden="true">
        <circle cx="12" cy="12" r="10" fill="none" stroke="var(--teal)" stroke-width="2"/>
        <ellipse cx="12" cy="12" rx="4.5" ry="10" fill="none" stroke="var(--teal)" stroke-width="1.5"/>
        <line x1="2" y1="12" x2="22" y2="12" stroke="var(--teal)" stroke-width="1.5"/>
        <line x1="4" y1="7" x2="20" y2="7" stroke="var(--teal)" stroke-width="1.2"/>
        <line x1="4" y1="17" x2="20" y2="17" stroke="var(--teal)" stroke-width="1.2"/>
      </svg>
      <span>www.yourdomain.com</span>
    </div>
  </main>
</body>
</html>
```